Leadership Conference Graphic Design Image

The Theme of our Conference is "Navigating Change. Driving Success." Attached is an AI example - What we are looking for is something along the lines of this image, but with realistic roads, a realistic semi truck (without being able to tell the make of the semi truck) and with the semi truck leaving dark skies and heading towards positive sunnier type skies. Please don't use the "Pinecrest Haulers Guild Yearly Convention" verbiage - Our event is called "Leadership Conference and Vendor Showcase". I've also attached our logo which we would like on the image as well - And we would like both vertical and horizontal designs. We will be using this on our stage and in printed materials.

```html
<!DOCTYPE html>
<html lang="en">
<head>
<meta charset="utf-8">
<title>Leadership Conference &amp; Vendor Showcase – Horizontal and Vertical Artwork</title>
<link href="https://fonts.googleapis.com/css2?family=Montserrat:ital,wght@0,800;1,700;1,800&display=swap" rel="stylesheet">
<style>
  :root {
    --page: #ffffff;
    --storm-dark: #1f242b;
    --storm: #363c45;
    --storm-mid: #5d6670;
    --sun: #ffd27a;
    --sun-core: #fff8e4;
    --amber: #e9a53c;
    --grass: #6f7a36;
    --road: #3f3b36;
    --road-light: #9a8c78;
    --haze: #f4f6f7;
    --road-blue: #5f7f95;
    --teal-dark: #2e4a58;
    --navy: #172636;
    --gold: #e3a614;
    --white: #ffffff;
  }
  * { box-sizing: border-box; margin: 0; padding: 0; }
  html, body { width: 1200px; height: 1200px; overflow: hidden; background: var(--page); }
  body { position: relative; font-family: "Montserrat", Arial, sans-serif; }

  .artwork { position: absolute; overflow: hidden; }
  .artwork--horizontal { left: 37px; top: 225px; width: 707px; height: 748px; }
  .artwork--vertical { left: 794px; top: 226px; width: 369px; height: 747px; }

  .scene-photo {
    position: absolute; inset: 0;
    background:
      radial-gradient(ellipse 16% 12% at 86% 26%, var(--sun-core) 0%, rgba(255,248,228,0) 100%),
      radial-gradient(ellipse 38% 26% at 84% 28%, rgba(255,210,122,.95) 0%, rgba(233,165,60,.6) 45%, rgba(233,165,60,0) 100%),
      radial-gradient(ellipse 45% 40% at 8% 30%, rgba(31,36,43,.9) 0%, rgba(31,36,43,0) 100%),
      radial-gradient(ellipse 22% 14% at 95% 50%, rgba(111,122,54,.85) 0%, rgba(111,122,54,0) 100%),
      radial-gradient(ellipse 75% 16% at 50% 72%, rgba(255,255,255,1) 0%, rgba(255,255,255,.7) 45%, rgba(255,255,255,0) 100%),
      radial-gradient(ellipse 60% 14% at 55% 62%, rgba(233,165,60,.55) 0%, rgba(233,165,60,0) 100%),
      linear-gradient(180deg, var(--storm-dark) 0%, var(--storm) 14%, var(--storm-mid) 30%, #8a7f68 42%, var(--road) 54%, var(--road-light) 64%, var(--haze) 74%, #e4ebef 82%, var(--road-blue) 93%, var(--teal-dark) 100%);
  }

  .tagline {
    position: absolute; left: 0; right: 0; text-align: center;
    color: var(--white); font-weight: 800; font-style: italic; line-height: 1.1;
    text-shadow: 0 2px 6px rgba(0,0,0,.5);
  }
  .light-streak { position: absolute; left: 0; width: 100%; }

  .event-title { position: absolute; left: 0; right: 0; text-align: center; color: var(--navy); font-weight: 800; line-height: 1; }
  .event-title__lead { display: block; font-style: italic; }
  .event-title__main { display: block; }
  .event-title__sub { display: block; color: var(--gold); font-weight: 700; font-style: italic; }

  .host { position: absolute; left: 0; right: 0; text-align: center; color: var(--navy); font-weight: 800; }
  .host__name { display: block; line-height: 1; }
  .host__full { display: block; font-size: 7px; letter-spacing: 1px; margin-top: 4px; }

  /* horizontal sizes */
  .artwork--horizontal .tagline { top: 48px; font-size: 40px; }
  .artwork--horizontal .light-streak { top: 140px; }
  .artwork--horizontal .event-title { top: 391px; }
  .artwork--horizontal .event-title__lead { font-size: 80px; }
  .artwork--horizontal .event-title__main { font-size: 67px; margin-top: -9px; }
  .artwork--horizontal .event-title__sub { font-size: 36px; margin-top: 2px; }
  .artwork--horizontal .host { top: 619px; }
  .artwork--horizontal .host__name { font-size: 56px; }

  /* vertical sizes */
  .artwork--vertical .tagline { top: 78px; font-size: 30px; }
  .artwork--vertical .light-streak { top: 152px; }
  .artwork--vertical .event-title { top: 524px; }
  .artwork--vertical .event-title__lead { font-size: 48px; }
  .artwork--vertical .event-title__main { font-size: 41px; margin-top: -4px; }
  .artwork--vertical .event-title__sub { font-size: 22px; margin-top: 0; }
  .artwork--vertical .host { top: 674px; }
  .artwork--vertical .host__name { font-size: 40px; }
</style>
</head>
<body>

<section class="artwork artwork--horizontal">
  <div class="scene-photo" role="img" aria-label="Photo of a white semi truck on a winding highway, driving out of dark stormy skies toward a bright golden sunrise, with light streaks on the road below"></div>
  <p class="tagline">Navigating Change.<br>Driving Success.</p>
  <svg class="light-streak" height="40" viewBox="0 0 707 40" aria-hidden="true">
    <path d="M220 32 C330 12 470 6 560 10" fill="none" stroke="#f0b42a" stroke-width="4" stroke-linecap="round" opacity=".85"/>
  </svg>
  <h1 class="event-title">
    <span class="event-title__lead">LEADERSHIP</span>
    <span class="event-title__main">CONFERENCE</span>
    <span class="event-title__sub">&amp; VENDOR SHOWCASE</span>
  </h1>
  <div class="host">
    <span class="host__name">PHG</span>
    <span class="host__full">PINECREST HAULERS GUILD</span>
  </div>
</section>

<section class="artwork artwork--vertical">
  <div class="scene-photo" role="img" aria-label="Photo of a white semi truck on a winding highway, driving out of dark stormy skies toward a bright golden sunrise, with light streaks on the road below"></div>
  <p class="tagline">Navigating Change.<br>Driving Success.</p>
  <svg class="light-streak" height="30" viewBox="0 0 369 30" aria-hidden="true">
    <path d="M70 24 C150 10 260 4 340 8" fill="none" stroke="#f0b42a" stroke-width="3" stroke-linecap="round" opacity=".85"/>
  </svg>
  <h2 class="event-title">
    <span class="event-title__lead">LEADERSHIP</span>
    <span class="event-title__main">CONFERENCE</span>
    <span class="event-title__sub">&amp; VENDOR SHOWCASE</span>
  </h2>
  <div class="host">
    <span class="host__name">PHG</span>
    <span class="host__full">PINECREST HAULERS GUILD</span>
  </div>
</section>

</body>
</html>
```